Business Cards

Need a neat design for a new business card

Industry/Entity Type

Residential Construction

Contact Information for Business Card

Company Name- KOVE Construction Inc.
Owner- Marcus Tolliver
Phone number- (555)203-7481
Email- kovecohomes@brindlemail.example
Facebook- www.socialpage.example/kovecohomes

Colors
fefdec

```html
<!DOCTYPE html>
<html lang="en">
<head>
<meta charset="utf-8">
<title>KOVE Construction Inc. – Business Card</title>
<link rel="stylesheet" href="https://fonts.googleapis.com/css2?family=Roboto:wght@400;500;700&display=swap">
<style>
  :root {
    --backdrop: #3b3c3e;
    --card: #ffffff;
    --ink: #111111;
    --muted: #8a8a8a;
    --rule: #b9b9b9;
  }
  * { box-sizing: border-box; margin: 0; padding: 0; }
  html, body {
    width: 1200px; height: 900px; overflow: hidden;
    background: var(--backdrop);
    font-family: "Roboto", Arial, sans-serif;
    color: var(--ink);
  }
  .sheet {
    width: 1200px; height: 900px;
    display: flex; flex-direction: column;
    align-items: center; justify-content: center;
    gap: 36px;
  }
  .card {
    width: 700px; height: 400px;
    background: var(--card);
    border-radius: 34px;
    position: relative;
    display: flex; align-items: center;
  }
  .card--front { justify-content: center; }

  .wordmark {
    display: flex; align-items: center; gap: 16px;
  }
  .wordmark__square {
    width: 30px; height: 30px; background: var(--ink);
  }
  .wordmark__name {
    font-weight: 500; color: var(--ink);
    line-height: 1.05; letter-spacing: 0.14em;
  }
  .wordmark__name .line-main { display: block; font-size: 56px; }
  .wordmark__name .line-sub { display: block; font-size: 17px; letter-spacing: 0.32em; margin-top: 6px; }

  .card--back .wordmark { position: absolute; left: 70px; top: 150px; }
  .card--back .wordmark__square { width: 24px; height: 24px; }
  .card--back .wordmark__name .line-main { font-size: 46px; }
  .card--back .wordmark__name .line-sub { font-size: 14px; }

  .divider {
    position: absolute; left: 372px; top: 110px;
    width: 1px; height: 180px; background: var(--rule);
  }
  .contact {
    position: absolute; left: 400px; top: 118px;
  }
  .contact__name {
    font-weight: 700; font-size: 20px; letter-spacing: 0.02em;
  }
  .contact__role {
    font-size: 14px; color: var(--muted); margin-top: 2px; margin-bottom: 22px;
  }
  .contact__row {
    display: flex; align-items: center; gap: 12px;
    font-size: 14.5px; margin-bottom: 14px; white-space: nowrap;
  }
  .contact__icon {
    width: 22px; height: 22px; background: var(--ink);
    display: flex; align-items: center; justify-content: center; flex: none;
  }
</style>
</head>
<body>
<main class="sheet">

  <section class="card card--front" aria-label="Card front">
    <div class="wordmark">
      <span class="wordmark__square"></span>
      <span class="wordmark__name">
        <span class="line-main">KOVE</span>
        <span class="line-sub">CONSTRUCTION</span>
      </span>
    </div>
  </section>

  <section class="card card--back" aria-label="Card back">
    <div class="wordmark">
      <span class="wordmark__square"></span>
      <span class="wordmark__name">
        <span class="line-main">KOVE</span>
        <span class="line-sub">CONSTRUCTION</span>
      </span>
    </div>

    <span class="divider"></span>

    <div class="contact">
      <p class="contact__name">MARCUS TOLLIVER</p>
      <p class="contact__role">Owner</p>

      <p class="contact__row">
        <span class="contact__icon">
          <svg width="14" height="14" viewBox="0 0 24 24" aria-hidden="true">
            <path fill="#fff" d="M6.6 10.8a15.1 15.1 0 0 0 6.6 6.6l2.2-2.2a1 1 0 0 1 1-.25 11.4 11.4 0 0 0 3.6.57 1 1 0 0 1 1 1V20a1 1 0 0 1-1 1A17 17 0 0 1 3 4a1 1 0 0 1 1-1h3.5a1 1 0 0 1 1 1c0 1.25.2 2.45.57 3.6a1 1 0 0 1-.25 1z"/>
          </svg>
        </span>
        (555)203-7481
      </p>
      <p class="contact__row">
        <span class="contact__icon">
          <svg width="14" height="12" viewBox="0 0 24 18" aria-hidden="true">
            <rect x="1" y="1" width="22" height="16" fill="none" stroke="#fff" stroke-width="2"/>
            <path d="M1 1l11 9 11-9" fill="none" stroke="#fff" stroke-width="2"/>
          </svg>
        </span>
        kovecohomes@brindlemail.example
      </p>
      <p class="contact__row">
        <span class="contact__icon"></span>
        www.socialpage.example/kovecohomes
      </p>
    </div>
  </section>

</main>
</body>
</html>
```